Letterhead and business cards for criminal defense law firm
with existing logo
Letterhead and business cards for criminal defense law firm - Law
Creative Brief
Simple
The Law Office of Marcus Varek, PLLC
718 Birchwood Avenue, Suite 300 Houston, TX 77019
Varek@BrightCounselGroup.net
I would like to incorporate our slogan: Experienced criminal defense lawyers Or if you think of a better slogan/motto, feel free to incorporate it. I am not a flashy or showy lawyer. I want the card to invoke credibility, stability and intelligence (not an ambulance chaser or sleazy lawyer).

```html
<!DOCTYPE html>
<html lang="en">
<head>
<meta charset="utf-8">
<title>Marcus Varek, PLLC – Stationery</title>
<link rel="stylesheet" href="https://fonts.googleapis.com/css2?family=Montserrat:wght@400;600;700&family=Open+Sans:wght@400;600&display=swap">
<style>
  :root {
    --navy: #2d2f4e;
    --paper: #ffffff;
    --backdrop: #ececed;
    --shade: #d9d9dc;
    --ink-soft: #6b6c7a;
    --mark-faint: #e6e6e9;
  }
  * { box-sizing: border-box; margin: 0; padding: 0; }
  html, body { width: 1200px; height: 936px; overflow: hidden; }
  body {
    background: var(--backdrop);
    position: relative;
    font-family: "Open Sans", Arial, sans-serif;
    color: var(--navy);
  }
  .sheet {
    position: absolute;
    background: var(--paper);
    box-shadow: 0 2px 6px rgba(0,0,0,0.12);
    overflow: hidden;
  }
  .band { position: absolute; left: 0; bottom: 0; width: 100%; display: block; }
  .band-url {
    position: absolute; left: 0; width: 100%; text-align: center;
    color: var(--paper); font-family: "Montserrat", Arial, sans-serif; font-weight: 600;
  }
  .brand { display: flex; align-items: center; gap: 6px; }
  .brand-square { background: var(--navy); flex: none; }
  .brand-name {
    font-family: "Montserrat", Arial, sans-serif; font-weight: 700;
    color: var(--navy); letter-spacing: 0.04em; white-space: nowrap;
  }
  .fine { font-size: 6px; line-height: 1.55; color: var(--ink-soft); }

  /* Letterhead */
  .letterhead { left: 183px; top: 69px; width: 388px; height: 546px; }
  .letterhead .brand { position: absolute; left: 14px; top: 14px; }
  .letterhead .brand-square { width: 26px; height: 26px; }
  .letterhead .brand-name { font-size: 15px; }
  .letterhead .contact { position: absolute; right: 18px; top: 14px; width: 118px; }
  .letterhead .contact p::before {
    content: ""; display: inline-block; width: 4px; height: 4px;
    background: var(--navy); margin-right: 4px; vertical-align: middle;
  }
  .letterhead .faint-mark {
    position: absolute; left: 157px; top: 224px; width: 74px; height: 74px;
    background: var(--mark-faint);
  }
  .letterhead .band-url { bottom: 10px; font-size: 11px; }

  /* Folder */
  .folder { left: 635px; top: 38px; width: 462px; height: 577px; }
  .folder .lockup { position: absolute; left: 0; top: 210px; width: 100%; text-align: center; }
  .folder .brand-square { width: 70px; height: 62px; margin: 0 auto 10px; }
  .folder .kicker {
    font-family: "Montserrat", Arial, sans-serif; font-size: 9px; letter-spacing: 0.12em;
    color: var(--ink-soft); text-transform: uppercase;
  }
  .folder .brand-name { font-size: 34px; display: block; line-height: 1.15; }
  .folder .suffix { font-size: 8px; letter-spacing: 0.2em; color: var(--ink-soft); }
  .folder .rule { width: 210px; height: 1px; background: var(--navy); margin: 3px auto; }
  .folder .band-url { bottom: 12px; font-size: 13px; }

  /* Business cards */
  .card { left: 41px; width: 183px; height: 107px; border-radius: 4px; }
  .card-front { top: 655px; }
  .card-back { top: 782px; }
  .card-front .brand { position: absolute; left: 10px; top: 10px; gap: 4px; }
  .card-front .brand-square { width: 14px; height: 14px; }
  .card-front .brand-name { font-size: 8px; }
  .card-front .person { position: absolute; left: 10px; top: 40px; }
  .card-front .person strong { font-size: 7px; display: block; color: var(--navy); }
  .card-front .person span { font-size: 5px; color: var(--ink-soft); }
  .card-front .contact { position: absolute; left: 96px; top: 36px; font-size: 4.5px; }
  .card-back .site {
    position: absolute; left: 0; top: 40px; width: 100%; text-align: center;
    font-family: "Montserrat", Arial, sans-serif; font-weight: 600; font-size: 8px;
  }

  /* Envelope front */
  .envelope { left: 269px; top: 668px; width: 442px; height: 216px; }
  .envelope .brand { position: absolute; left: 16px; top: 16px; }
  .envelope .brand-square { width: 26px; height: 26px; }
  .envelope .brand-name { font-size: 16px; }
  .envelope .return-address { position: absolute; left: 16px; top: 48px; font-size: 6.5px; color: var(--ink-soft); }

  /* Envelope back */
  .envelope-back { left: 742px; top: 668px; width: 429px; height: 216px; }
  .envelope-back .site {
    position: absolute; left: 0; top: 28px; width: 100%; text-align: center;
    font-family: "Montserrat", Arial, sans-serif; font-weight: 600; font-size: 11px;
  }
  .envelope-back .flap { position: absolute; left: 0; top: 0; width: 100%; height: 100%; }
</style>
</head>
<body>

  <section class="sheet letterhead" aria-label="Letterhead">
    <div class="brand">
      <span class="brand-square"></span>
      <span class="brand-name">MARCUS VAREK</span>
    </div>
    <div class="contact fine">
      <p>718 Birchwood Avenue, Suite 300</p>
      <p>Houston, TX 77019</p>
      <p>T: (713) 555-0148</p>
      <p>F: (713) 555-0149</p>
      <p>Varek@BrightCounselGroup.net</p>
    </div>
    <div class="faint-mark"></div>
    <svg class="band" viewBox="0 0 388 60" height="60" preserveAspectRatio="none">
      <path d="M0 22 Q194 -6 388 16 L388 60 L0 60 Z" fill="#d9d9dc"/>
      <path d="M0 30 Q194 4 388 24 L388 60 L0 60 Z" fill="#2d2f4e"/>
    </svg>
    <p class="band-url">www.BrightCounselGroup.net</p>
  </section>

  <section class="sheet folder" aria-label="Presentation folder">
    <div class="lockup">
      <div class="brand-square"></div>
      <p class="kicker">The Law Office of</p>
      <div class="rule"></div>
      <span class="brand-name">MARCUS VAREK</span>
      <div class="rule"></div>
      <p class="suffix">PLLC</p>
    </div>
    <svg class="band" viewBox="0 0 462 64" height="64" preserveAspectRatio="none">
      <path d="M0 14 Q231 -8 462 22 L462 64 L0 64 Z" fill="#d9d9dc"/>
      <path d="M0 22 Q231 2 462 30 L462 64 L0 64 Z" fill="#2d2f4e"/>
    </svg>
    <p class="band-url">www.BrightCounselGroup.net</p>
  </section>

  <section class="sheet card card-front" aria-label="Business card front">
    <div class="brand">
      <span class="brand-square"></span>
      <span class="brand-name">MARCUS VAREK</span>
    </div>
    <div class="person">
      <strong>Marcus Varek</strong>
      <span>Attorney at Law</span>
    </div>
    <div class="contact fine">
      <p>718 Birchwood Avenue, Suite 300</p>
      <p>Houston, TX 77019</p>
      <p>T: (713) 555-0148</p>
      <p>F: (713) 555-0149</p>
      <p>Varek@BrightCounselGroup.net</p>
    </div>
    <svg class="band" viewBox="0 0 183 16" height="16" preserveAspectRatio="none">
      <path d="M0 6 Q92 0 183 5 L183 16 L0 16 Z" fill="#2d2f4e"/>
    </svg>
  </section>

  <section class="sheet card card-back" aria-label="Business card back">
    <p class="site">www.BrightCounselGroup.net</p>
    <svg class="band" viewBox="0 0 183 16" height="16" preserveAspectRatio="none">
      <path d="M0 6 Q92 0 183 5 L183 16 L0 16 Z" fill="#2d2f4e"/>
    </svg>
  </section>

  <section class="sheet envelope" aria-label="Envelope front">
    <div class="brand">
      <span class="brand-square"></span>
      <span class="brand-name">MARCUS VAREK</span>
    </div>
    <p class="return-address">718 Birchwood Avenue, Suite 300 Houston, TX 77019</p>
  </section>

  <section class="sheet envelope-back" aria-label="Envelope back">
    <svg class="flap" viewBox="0 0 429 216" preserveAspectRatio="none">
      <path d="M0 58 Q214 40 429 58 L429 70 L214 150 L0 70 Z" fill="#d9d9dc"/>
      <path d="M0 64 Q214 46 429 64 L429 216 L0 216 L0 64 Z" fill="#ffffff"/>
      <path d="M0 64 L214 146 L429 64 L429 76 L214 158 L0 76 Z" fill="#2d2f4e"/>
      <path d="M0 64 Q214 46 429 64 L429 0 L0 0 Z" fill="#ffffff"/>
      <path d="M0 64 Q214 46 429 64 L214 146 Z" fill="#2d2f4e"/>
    </svg>
    <p class="site">www.BrightCounselGroup.net</p>
  </section>

</body>
</html>
```